Business Card Design

Consultant ot credit unions that operate a property and casualty insurance agency

Industry/Entity Type

Insurance

Contact Information for Business Card

Dorian Velker
Credit Union Insurance Agency Consultant
dorianvelker@mailvoro.com
562 318-4092
914 Tamsin Court
Long Beach, CA 90813

```html
<!DOCTYPE html>
<html lang="en">
<head>
<meta charset="UTF-8">
<title>Dorian Velker — Business Card</title>
<link rel="stylesheet" href="https://fonts.googleapis.com/css2?family=Arimo:wght@700&family=Jost:wght@300;400&display=swap">
<style>
  :root {
    --backdrop: #dadada;
    --card: #ffffff;
    --brand-blue: #1b75bb;
    --on-blue: #ffffff;
  }
  * { margin: 0; padding: 0; box-sizing: border-box; }
  html, body {
    width: 1200px;
    height: 720px;
    overflow: hidden;
    background: var(--backdrop);
  }
  .canvas {
    position: relative;
    width: 1200px;
    height: 720px;
  }
  .card {
    position: absolute;
    width: 516px;
    height: 304px;
    background: var(--card);
    overflow: hidden;
  }
  .card--front { left: 62px; top: 208px; }
  .card--back  { left: 626px; top: 210px; }

  .identity {
    position: absolute;
    left: 0; right: 0;
    top: 72px;
    text-align: center;
  }
  .identity__name {
    font-family: "Arimo", Arial, sans-serif;
    font-weight: 700;
    font-size: 38px;
    letter-spacing: 2.5px;
    color: var(--brand-blue);
    line-height: 1;
    text-transform: uppercase;
  }
  .identity__title {
    margin-top: 16px;
    font-family: "Jost", sans-serif;
    font-weight: 300;
    font-size: 21px;
    color: var(--brand-blue);
    line-height: 1;
  }

  .contact-band {
    position: absolute;
    left: 0; right: 0; bottom: 0;
    height: 92px;
    background: var(--brand-blue);
    display: flex;
  }
  .contact-band__column {
    flex: 1;
    padding: 18px 0 0 24px;
  }
  .contact-band__column + .contact-band__column {
    border-left: 1.5px solid var(--on-blue);
  }
  .contact-item {
    position: relative;
    padding-left: 22px;
    font-family: "Jost", sans-serif;
    font-weight: 300;
    font-size: 13.5px;
    line-height: 18px;
    letter-spacing: 0.3px;
    color: var(--on-blue);
  }
  .contact-item::before {
    content: "";
    position: absolute;
    left: 0; top: 5px;
    width: 8px; height: 8px;
    border-radius: 50%;
    background: var(--on-blue);
  }
  .contact-item + .contact-item { margin-top: 13px; }
</style>
</head>
<body>
  <main class="canvas">
    <section class="card card--front" aria-label="Business card front">
      <header class="identity">
        <h1 class="identity__name">Dorian Velker</h1>
        <p class="identity__title">Credit Union / Insurance Agency Consultant</p>
      </header>
      <div class="contact-band">
        <div class="contact-band__column">
          <p class="contact-item">914 Tamsin Court Long Beach,<br>CA 90813</p>
        </div>
        <div class="contact-band__column">
          <p class="contact-item">dorianvelker@mailvoro.com</p>
          <p class="contact-item">562 318-4092</p>
        </div>
      </div>
    </section>
    <section class="card card--back" aria-label="Business card back"></section>
  </main>
</body>
</html>
```